Summit Builders Web Site / Business Cards

Construction Company that specializes in Water and Fire Damage, Residential ReModels, Landscaping and Building ADU (Accessory Dwelling Unit)

Growing and changing families often need additional space, and a remodeling project can often provide that. Adding a new area, or repurposing an existing one can satisfy this requirement.

Other times, homeowners want to update the look in their kitchen or bathroom with more than just a change of cabinetry or vanity doors and drawers. Whatever your needs are, Summit Builders has skilled workers who are bonded and insured, and ready to make your dreams and visions a reality.

Target Market(s)

Home Owners

Industry/Entity Type

Construction Company

Contact Information for Business Card

Center Logo with our information on the corners

Back side to be Logo Only
Contact Info
CSLB License # 4829516
info@summitbuildersca.example
www.summitbuildersca.example

Coding

Coded - Design and coding required

Number of Pages Required

5+ page

Font styles to use
Serif
Sans Serif

Requirements
Must have
• Using our Logo Colors
Home
About Us
Services
Projects / Portfolio
Contact Us
Nice to have
• Colors matching our Logo
Should not have
• Black because it doesnt match our logo

```html
<!DOCTYPE html>
<html lang="en">
<head>
<meta charset="utf-8">
<title>Summit Builders</title>
<link href="https://fonts.googleapis.com/css2?family=Poppins:wght@300;400;500;600;700;800&display=swap" rel="stylesheet">
<style>
:root{
  --orange:#f26a1b;
  --orange-deep:#d9530c;
  --ink:#262626;
  --charcoal:#2f2f2f;
  --text:#555;
  --mist:#f1f1f1;
  --white:#fff;
  --footer-text:#d6d6d6;
}
*{margin:0;padding:0;box-sizing:border-box}
html,body{width:1200px;height:4036px;overflow:hidden}
body{font-family:'Poppins',sans-serif;color:var(--ink);background:var(--white);position:relative}
.abs{position:absolute}
p{line-height:1.6}

/* header */
.topbar{left:0;top:0;width:1200px;height:48px;background:var(--white)}
.contact-strip{right:110px;top:14px;display:flex;gap:46px;font-size:14px;color:var(--text)}
.contact-strip span{display:flex;align-items:center;gap:8px}
.contact-strip svg{width:16px;height:16px}
.nav{left:0;top:48px;width:1200px;height:72px;background:var(--white)}
.nav ul{position:absolute;right:105px;top:22px;display:flex;gap:40px;list-style:none;font-size:16px}
.nav li.active{color:var(--orange);border-bottom:2px solid var(--orange);padding-bottom:4px}
.brand{left:130px;top:0;width:200px;height:140px;background:var(--white);border-radius:0 0 14px 14px;box-shadow:0 4px 14px rgba(0,0,0,.12);display:flex;flex-direction:column;align-items:center;justify-content:center;gap:8px}
.brand-mark{width:26px;height:26px;background:var(--orange)}
.brand-name{font-size:22px;font-weight:700;color:var(--ink);text-transform:uppercase;letter-spacing:1px;text-align:center;line-height:1.1}

/* hero */
.hero{left:0;top:120px;width:1200px;height:640px;background:linear-gradient(160deg,#6f7d86 0%,#9a8f7c 45%,#5a4a3a 100%)}
.hero-shade{left:0;top:120px;width:1200px;height:640px;background:rgba(20,20,20,.25)}
.hero-title{left:0;top:250px;width:1200px;text-align:center;color:var(--white)}
.hero-title h1{font-size:60px;font-weight:800;line-height:1.1}
.hero-title h2{font-size:44px;font-weight:600;line-height:1.2}
.hero-title p{font-size:20px;width:330px;margin:10px auto 0;line-height:1.4}
.btn{display:inline-flex;align-items:center;gap:14px;background:var(--ink);color:var(--white);border-radius:30px;padding:10px 10px 10px 28px;font-size:16px;font-weight:500}
.btn i{width:32px;height:32px;border-radius:50%;background:var(--orange);display:flex;align-items:center;justify-content:center}
.hero-btn{left:511px;top:490px}
.dots{display:flex;gap:8px}
.dots b{width:12px;height:12px;border-radius:50%;border:2px solid var(--white)}
.dots b.on{background:var(--white)}
.hero-dots{left:562px;top:630px}

/* about */
.about-art{left:120px;top:880px;width:350px;height:290px;background:linear-gradient(135deg,#f7f7f7,#e4e4e4);border-radius:6px}
.badge{left:140px;top:1060px;width:120px;height:64px;background:var(--orange);color:var(--white);display:flex;align-items:center;gap:8px;padding:0 12px}
.badge strong{font-size:36px;font-weight:700}
.badge span{font-size:12px;line-height:1.2}
.about-copy{left:615px;top:820px;width:470px}
.section-title{font-size:44px;font-weight:700}
.section-title em{font-style:normal;color:var(--orange)}
.about-copy .underline{width:60px;height:3px;background:var(--orange);margin:4px 0 20px}
.about-copy h3{font-size:26px;font-weight:700;margin-bottom:14px}
.about-copy p{font-size:14px;color:var(--text);margin-bottom:24px}

/* services */
.services{left:0;top:1260px;width:1200px;height:600px;background:linear-gradient(180deg,var(--orange) 0%,#f47e2f 60%,var(--orange-deep) 100%)}
.services-title{left:0;top:1320px;width:1200px;text-align:center;color:var(--white)}
.services-title h2{font-size:44px;font-weight:700}
.services-title p{font-size:17px;margin-top:4px}
.service{top:1450px;width:240px;text-align:center;color:var(--white)}
.service .icon{width:88px;height:88px;border-radius:50%;border:3px solid var(--white);margin:0 auto 22px;display:flex;align-items:center;justify-content:center}
.service h4{font-size:20px;font-weight:600;line-height:1.2;margin-bottom:8px}
.service p{font-size:15px;line-height:1.35;width:210px;margin:0 auto}
.arrow-side{top:1490px;width:30px;height:40px}

/* projects */
.projects{left:0;top:1880px;width:1200px;height:480px;background:var(--mist)}
.projects-copy{left:120px;top:2040px;width:300px}
.projects-copy h2{font-size:38px;font-weight:700;line-height:1.15;margin-bottom:18px}
.projects-copy p{font-size:14px;color:var(--text)}
.project-photo{top:2000px;width:310px;height:225px;box-shadow:0 10px 24px rgba(0,0,0,.2)}
.proj-dots{left:754px;top:2272px}
.proj-dots b{width:10px;height:10px;border-color:var(--orange)}
.proj-dots b.on{background:var(--orange)}

/* landmark */
.landmark-photo{left:610px;top:2380px;width:590px;height:460px;background:linear-gradient(120deg,#dfe3e6 0%,#b4bcc2 50%,#6b7780 100%)}
.landmark-frame{left:200px;top:2600px;width:410px;height:200px;border:3px solid var(--orange);border-right:none}
.landmark-copy{left:215px;top:2440px;width:385px}
.landmark-copy h2{font-size:34px;font-weight:700;line-height:1.25}
.values{left:230px;top:2630px;list-style:none}
.values li{display:flex;align-items:center;gap:14px;font-size:14px;text-transform:uppercase;color:var(--ink);margin-bottom:18px}
.values li i{width:14px;height:14px;border:2px solid var(--orange)}

/* stats */
.stats{left:0;top:2850px;width:1200px;height:360px;background:linear-gradient(180deg,#3a3a3a,#2a2a2a)}
.stat{top:2975px;width:240px;text-align:center;color:var(--white)}
.stat strong{display:block;font-size:44px;font-weight:600;line-height:1.1}
.stat span{font-size:24px}

/* clients */
.clients-title{left:0;top:3290px;width:1200px;text-align:center}
.clients-title h2{font-size:44px;font-weight:600}
.clients-title i{display:block;width:70px;height:3px;background:var(--orange);margin:6px auto 0}
.avatar{left:300px;top:3420px;width:120px;height:120px;border-radius:50%;background:linear-gradient(135deg,#d8c6b8,#8b6f5c)}
.quote-dot{left:300px;top:3440px;width:26px;height:26px;border-radius:50%;background:var(--orange)}
.testimonial{left:460px;top:3410px;width:330px}
.testimonial p{font-size:14px;color:var(--text)}
.testimonial cite{display:block;margin-top:18px;font-style:normal;font-size:14px;color:var(--orange);font-weight:500}
.client-arrows{left:805px;top:3540px;display:flex;gap:8px}

/* footer */
.footer{left:0;top:3760px;width:1200px;height:276px;background:var(--charcoal)}
.fcol{top:3790px;font-size:13px;line-height:1.9;color:var(--footer-text)}
.fcol h5{font-size:14px;font-weight:600;color:var(--white);margin-bottom:10px}
.fcol .line{display:flex;gap:10px;align-items:flex-start}
.fcol svg{width:14px;height:14px;margin-top:5px;flex:none}
.subscribe{display:flex;margin-top:14px}
.subscribe span{width:150px;height:34px;background:var(--white);color:#888;font-size:12px;padding:8px 12px}
.subscribe b{width:110px;height:34px;background:var(--orange);color:var(--white);font-size:13px;font-weight:500;display:flex;align-items:center;justify-content:center}
.footer-rule{left:120px;top:3960px;width:960px;height:1px;background:#555}
.copyright{left:120px;top:3982px;font-size:13px;display:flex;align-items:center;gap:16px;color:var(--footer-text)}
.copyright .brand-name{font-size:16px;color:var(--white)}
.social{left:995px;top:3982px;display:flex;gap:14px}
.social i{width:22px;height:22px;border-radius:50%;background:#ddd}
</style>
</head>
<body>

<header>
  <div class="abs topbar"></div>
  <div class="abs contact-strip">
    <span><svg viewBox="0 0 16 16"><path d="M3 1l3 3-2 2c1 2 3 4 5 5l2-2 3 3-2 3C6 15 1 10 1 3z" fill="#f26a1b"/></svg>(555) 010-2019</span>
    <span><svg viewBox="0 0 16 16"><path d="M3 1l3 3-2 2c1 2 3 4 5 5l2-2 3 3-2 3C6 15 1 10 1 3z" fill="#f26a1b"/></svg>+1 555 010 3491</span>
    <span><svg viewBox="0 0 16 16"><rect x="1" y="3" width="14" height="10" fill="none" stroke="#f26a1b" stroke-width="1.6"/><path d="M1 3l7 6 7-6" fill="none" stroke="#f26a1b" stroke-width="1.6"/></svg>hello@summitbuildersca.example</span>
  </div>
  <nav class="abs nav">
    <ul>
      <li class="active">Home</li><li>About Us</li><li>Services</li><li>Projects</li><li>Contact Us</li>
    </ul>
  </nav>
  <div class="abs brand"><i class="brand-mark"></i><span class="brand-name">Summit<br>Builders</span></div>
</header>

<section>
  <div class="abs hero" role="img" aria-label="Photo of construction workers on a site with cranes at sunset"></div>
  <div class="abs hero-shade"></div>
  <svg class="abs" style="left:0;top:620px" width="1200" height="150" viewBox="0 0 1200 150">
    <polygon points="0,60 600,120 1200,30 1200,150 0,150" fill="#fff"/>
    <polygon points="0,56 600,116 1200,26 1200,36 600,126 0,66" fill="#262626"/>
    <polygon points="0,30 260,56 260,66 0,40" fill="#f26a1b"/>
    <polygon points="940,66 1200,18 1200,28 940,76" fill="#f26a1b"/>
  </svg>
  <div class="abs hero-title">
    <h1>We Deliver</h1>
    <h2>Landmark Projects</h2>
    <p>Lorem Ipsum is simply dummy text of the printing and typesetting industry.</p>
  </div>
  <div class="abs hero-btn btn">Learn More <i><svg width="12" height="12" viewBox="0 0 12 12"><path d="M3 1l5 5-5 5" stroke="#fff" stroke-width="2" fill="none"/></svg></i></div>
  <div class="abs hero-dots dots"><b class="on"></b><b></b><b></b></div>
</section>

<section>
  <div class="abs about-art" role="img" aria-label="Illustration of an orange and charcoal office tower"></div>
  <div class="abs badge"><strong>12</strong><span>Years<br>Experience</span></div>
  <div class="abs about-copy">
    <h2 class="section-title">Who <em>We Are</em></h2>
    <div class="underline"></div>
    <h3>We Deliver Landmark Projects</h3>
    <p>We are skilled builders who care about every detail of your home. From the first plan to the final walkthrough, our bonded and insured crews repair, remodel and build with honest pricing, clear schedules and lasting craftsmanship you can trust.</p>
    <div class="btn">Learn More <i><svg width="12" height="12" viewBox="0 0 12 12"><path d="M3 1l5 5-5 5" stroke="#fff" stroke-width="2" fill="none"/></svg></i></div>
  </div>
</section>

<section>
  <div class="abs services" role="img" aria-label="Orange tinted photo of building scaffolding"></div>
  <svg class="abs" style="left:0;top:1240px" width="1200" height="60" viewBox="0 0 1200 60"><polygon points="0,0 1200,0 1200,20 0,50" fill="#fff"/></svg>
  <div class="abs services-title">
    <h2>Our Services</h2>
    <p>Lorem Ipsum is simply dummy text of the printing and typesetting industry.</p>
  </div>
  <svg class="abs arrow-side" style="left:90px" viewBox="0 0 30 40"><path d="M22 4L6 20l16 16" stroke="#fff" stroke-width="5" fill="none"/></svg>
  <svg class="abs arrow-side" style="left:1080px" viewBox="0 0 30 40"><path d="M8 4l16 16L8 36" stroke="#fff" stroke-width="5" fill="none"/></svg>

  <div class="abs service" style="left:150px">
    <div class="icon"><svg width="44" height="44" viewBox="0 0 44 44"><path d="M22 4c8 10 12 16 12 22a12 12 0 0 1-24 0c0-6 4-12 12-22z" fill="none" stroke="#fff" stroke-width="3"/></svg></div>
    <h4>Water and<br>Fire Damage</h4>
    <p>Lorem Ipsum is simply dummy text of the printing and typesetting industry.</p>
  </div>
  <div class="abs service" style="left:480px">
    <div class="icon"><svg width="44" height="44" viewBox="0 0 44 44"><path d="M6 22L22 8l16 14M11 19v17h22V19" fill="none" stroke="#fff" stroke-width="3"/></svg></div>
    <h4>Residential<br>ReModels</h4>
    <p>Lorem Ipsum is simply dummy text of the printing and typesetting industry.</p>
  </div>
  <div class="abs service" style="left:810px">
    <div class="icon"><svg width="44" height="44" viewBox="0 0 44 44"><path d="M4 24L22 10l18 14M10 20v16h8v-9h8v9h8V20" fill="none" stroke="#fff" stroke-width="3"/></svg></div>
    <h4>Landscaping and<br>Building</h4>
    <p>Lorem Ipsum is simply dummy text of the printing and typesetting industry.</p>
  </div>
  <svg class="abs" style="left:0;top:1780px" width="1200" height="100" viewBox="0 0 1200 100">
    <polygon points="0,100 530,100 600,30 670,100 1200,100 1200,100" fill="#f1f1f1"/>
    <polygon points="600,20 690,100 670,100 600,38 530,100 510,100" fill="#262626"/>
  </svg>
</section>

<section>
  <div class="abs projects"></div>
  <div class="abs projects-copy">
    <h2>RECENT<br>PROJECTS</h2>
    <p>Lorem Ipsum is simply dummy text of the printing and typesetting industry. Lorem Ipsum has been the industry's.</p>
  </div>
  <div class="abs project-photo" style="left:450px;background:linear-gradient(180deg,#8fc0e8 0%,#7fae5a 60%,#3b6d3a 100%)" role="img" aria-label="Photo of a finished two-storey home with garden"></div>
  <div class="abs project-photo" style="left:775px;background:linear-gradient(180deg,#5d86c4 0%,#b79a86 55%,#6c8a52 100%)" role="img" aria-label="Photo of a brick family house with front lawn"></div>
  <div class="abs proj-dots dots"><b></b><b class="on"></b><b></b></div>
</section>

<section>
  <div class="abs landmark-photo" role="img" aria-label="Photo of two businessmen shaking hands in an office"></div>
  <div class="abs landmark-frame"></div>
  <div class="abs landmark-copy"><h2>WE DELIVER<br>LANDMARK PROJECTS</h2></div>
  <ul class="abs values">
    <li><i></i>We've Repution For Excellence</li>
    <li><i></i>We Build Partnerships</li>
    <li><i></i>Guided By Commitment</li>
    <li><i></i>A Team Of Professionals</li>
  </ul>
</section>

<section>
  <div class="abs stats" role="img" aria-label="Dark tinted photo of construction tools"></div>
  <svg class="abs" style="left:0;top:2840px" width="1200" height="60" viewBox="0 0 1200 60">
    <polygon points="0,0 1200,0 1200,10 0,40" fill="#fff"/>
    <polygon points="900,18 1200,10 1200,16 900,24" fill="#f26a1b"/>
  </svg>
  <svg class="abs" style="left:0;top:3150px" width="1200" height="70" viewBox="0 0 1200 70">
    <polygon points="0,70 0,50 1200,0 1200,70" fill="#fff"/>
    <polygon points="0,40 380,24 380,32 0,48" fill="#f26a1b"/>
  </svg>
  <div class="abs stat" style="left:95px"><strong>53</strong><span>Total Projects</span></div>
  <div class="abs stat" style="left:360px"><strong>371</strong><span>Staff Members</span></div>
  <div class="abs stat" style="left:640px"><strong>15</strong><span>Working In States</span></div>
  <div class="abs stat" style="left:900px"><strong>2,600</strong><span>Hours For Work</span></div>
</section>

<section>
  <div class="abs clients-title"><h2>Our Clients</h2><i></i></div>
  <div class="abs avatar" role="img" aria-label="Client portrait"></div>
  <div class="abs quote-dot"></div>
  <div class="abs testimonial">
    <p>This is due to their excellent service, competitive pricing and customer support. It's thoroughly refreshing to get such a personal touch.</p>
    <cite>Dana Reyes</cite>
  </div>
  <svg class="abs client-arrows" width="60" height="20" viewBox="0 0 60 20">
    <path d="M24 10H4m6-6l-6 6 6 6" stroke="#f26a1b" stroke-width="2" fill="none"/>
    <path d="M36 10h20m-6-6l6 6-6 6" stroke="#999" stroke-width="2" fill="none"/>
  </svg>
</section>

<footer>
  <div class="abs footer"></div>
  <div class="abs fcol" style="left:120px;width:260px">
    <h5>Contact Us</h5>
    <div class="line"><svg viewBox="0 0 14 14"><path d="M7 1a4 4 0 0 1 4 4c0 3-4 8-4 8S3 8 3 5a4 4 0 0 1 4-4z" fill="#f26a1b"/></svg><span>480 Ridge Avenue, Suite 12,<br>Fairview CA 90210</span></div>
    <div class="line"><svg viewBox="0 0 16 16"><path d="M3 1l3 3-2 2c1 2 3 4 5 5l2-2 3 3-2 3C6 15 1 10 1 3z" fill="#f26a1b"/></svg><span>(555) 010-7788</span></div>
    <div class="line"><svg viewBox="0 0 16 16"><rect x="1" y="3" width="14" height="10" fill="none" stroke="#f26a1b" stroke-width="1.6"/><path d="M1 3l7 6 7-6" fill="none" stroke="#f26a1b" stroke-width="1.6"/></svg><span>office@summitbuildersca.example</span></div>
  </div>
  <div class="abs fcol" style="left:410px">
    <h5>QUICK LINKS</h5><div>Home</div><div>Company</div><div>Projects</div>
  </div>
  <div class="abs fcol" style="left:615px">
    <h5>QUICK LINKS</h5><div>Services</div><div>Contact Us</div><div>Teams</div>
  </div>
  <div class="abs fcol" style="left:825px;width:270px">
    <h5>WRITE TO US</h5>
    <div style="line-height:1.5">Provide your email below to<br>subscribe to our newsletter</div>
    <div class="subscribe"><span>Email address</span><b>Subscribe</b></div>
  </div>
  <div class="abs footer-rule"></div>
  <div class="abs copyright"><span>Copyright 2020</span><span class="brand-name">Summit Builders</span><span>All Rights Reserved.</span></div>
  <div class="abs social"><i></i><i></i><i></i></div>
</footer>

</body>
</html>
```